Dieser Designer hat seinen Job wirklich makellos erledigt. Er war auch bei der Menge an Anforderungen, die ich an ihn hatte, sehr geduldig und wurde allen Anforderungen mehr als gerecht. Ich wäre sehr erfreut, wenn ich in der Zukunft wieder mit ihm arbeiten kann. Ich sehe eine helle Zukunft für diesen Designer und kann ihn nur jedem weiterempfehlen, der Wert auf sein Produkt legt.
Zielgruppe
Genre: Ratgeber
Autorenname: Kilian Sturmfeld
Titel: Staatswesen klar gemacht
Untertitel: Wie Sie endlich mitreden, Ihr Wissen über die deutsche Politik auffrischen und das Land mitgestalten können - Das Politik Buch für Einsteiger
Zielgruppe:
- Personen die Schwierigkeiten haben nachzuvollziehen, was in der Politik geschieht
- Personen die keine Zeit haben, sich durch Nachschlagewerke und co. zu wälzen
- Personen, denen die Wahlentscheidung aufgrund, deren mangelnden Wissens schwer fällt
- Personen, denen das fehlende Wissen über die Politik im Alltag langsam peinlich sind
- Personen, die ihre Meinung in politischen Diskussionen nicht zum Ausdrück bringen können
- Personen, die sich als einzelne machtlos fühlen
- Personen, die mit der politischen Lage unzufrieden sind, jedoch nicht wissen, was wie sein soll
- Personen, die dachten, Politik ist zu langweilig und trocken um sich damit auseinander zu setzen
- Männlich und Weiblich ausgeglichene Zielgruppe
- U.a. junge Leser
Aufgabenstellung
Das ist das Besondere an meinem Buch:
- Die Leser dieses Buches werden in der schnellstmöglichen Zeit ihre politische Unwissenheit besiegen, ohne dass ihnen langweilig wird.
Das sollte meine Leser beim Cover fühlen:
- Sie sollen beim ansehen des Covers das Verlangen verspüren, die Details des Covers erkunden zu wollen.
- Sie sollen sofort erkennen, worum es in dem Buch geht
Das möchte ich besonders hervorheben:
- Ich möchte hervorheben, dass dieses Buch das hochwertigste Buch dieser Thematik ist.
Ich bevorzuge folgende Farben: Helle Farben
Verlagsname und Autorenname dort einfügen wo es am besten passt.
Fonts: Frei Wählbar
Format: Geplant sind 13,34 x 20,32 cm.
Weitere Vorgaben:
- Keine Bilder von echten Personen verwenden
- Seit Kreativ und gestaltet ein ins Auge springendes Cover

```html
<!DOCTYPE html>
<html lang="de">
<head>
<meta charset="utf-8">
<title>Staatswesen klar gemacht – Buchumschlag</title>
<link rel="stylesheet" href="https://fonts.googleapis.com/css2?family=Oswald:wght@500;700&family=Roboto:wght@400;500&display=swap">
<style>
  :root {
    --stage: #e4e3e1;
    --orange: #ef7c38;
    --orange-deep: #e3661f;
    --panel: #e06020;
    --white: #ffffff;
    --ink: #3a2a20;
    --photo-tone: #a9a29b;
    --art-red: #c8322b;
    --art-lime: #cfe23a;
  }
  * { box-sizing: border-box; margin: 0; padding: 0; }
  html, body { width: 1200px; height: 800px; overflow: hidden; }
  body { background: var(--stage); font-family: "Roboto", Arial, sans-serif; position: relative; }

  .cover-wrap {
    position: absolute; left: 155px; top: 80px;
    width: 890px; height: 640px; display: flex;
    box-shadow: 0 8px 24px rgba(0,0,0,.15);
  }
  .back, .front { position: relative; width: 420px; height: 640px; background: var(--orange); }
  .spine { position: relative; width: 50px; height: 640px; background: var(--orange-deep); }

  /* Back cover */
  .author-photo {
    position: absolute; left: 34px; top: 54px; width: 82px; height: 88px;
    background: linear-gradient(160deg, #c9c3bc, var(--photo-tone));
    z-index: 2; border: 2px solid rgba(255,255,255,.3);
  }
  .blurb-panel {
    position: absolute; left: 34px; top: 98px; width: 340px; height: 440px;
    background: var(--panel); color: var(--white); padding: 112px 26px 20px 26px;
  }
  .blurb-heading {
    position: absolute; left: 100px; top: 22px; font-size: 13px; line-height: 1.25;
    font-weight: 400; text-transform: uppercase; letter-spacing: .02em;
  }
  .blurb-panel p { font-size: 10.5px; line-height: 1.4; margin-bottom: 12px; }
  .blurb-call {
    text-align: center; text-transform: uppercase; font-size: 12.5px; line-height: 1.35; margin-top: 6px;
  }
  .blurb-call span { display: block; }
  .blurb-call span:first-child { margin-bottom: 6px; }

  /* Spine */
  .spine-title {
    position: absolute; left: 50%; top: 30px;
    transform: translateX(-50%); writing-mode: vertical-rl;
    white-space: nowrap; color: var(--white);
    font-family: "Oswald", "Arial Narrow", sans-serif; font-weight: 700; font-size: 24px;
  }
  .spine-title small { font-size: 19px; font-weight: 500; margin-right: 40px; }
  .spine-author {
    position: absolute; bottom: 18px; left: 0; right: 0; text-align: center;
    color: var(--white); font-size: 9px; line-height: 1.2;
  }

  /* Front cover */
  .publisher {
    position: absolute; top: 18px; right: 16px; color: var(--white);
    font-size: 15px; font-weight: 500;
  }
  .title {
    position: absolute; top: 44px; left: 0; right: 0; text-align: center;
    font-family: "Oswald", "Arial Narrow", sans-serif; font-weight: 700;
    color: var(--white); text-transform: uppercase; line-height: 1;
  }
  .title-line { display: block; font-size: 72px; }
  .title-line.long { font-size: 54px; }
  .title-meta {
    display: block; font-family: "Roboto", Arial, sans-serif; font-weight: 400;
    text-transform: none; font-size: 11px; color: var(--ink); margin: 2px 0 6px;
  }
  .cover-art {
    position: absolute; left: 90px; top: 300px; width: 240px; height: 200px;
    background: linear-gradient(135deg, #f39a5c 0%, #f0b070 40%, var(--art-red) 75%, var(--art-lime) 100%);
    opacity: .85; border-radius: 6px;
  }
  .tagline {
    position: absolute; top: 512px; left: 0; right: 0; text-align: center;
    font-family: "Oswald", "Arial Narrow", sans-serif; font-weight: 700;
    color: var(--white); font-size: 21px; line-height: 1.2;
  }
  .subtitle {
    position: absolute; top: 580px; left: 14px; right: 14px; text-align: center;
    color: var(--white); font-size: 10.5px; line-height: 1.35;
  }
</style>
</head>
<body>
  <div class="cover-wrap">
    <section class="back">
      <div class="author-photo" role="img" aria-label="Autorenfoto von Kilian Sturmfeld"></div>
      <div class="blurb-panel">
        <h2 class="blurb-heading">Souverän<br>und sicher<br>durch jedes<br>Politikgespräch</h2>
        <p>Dank „Staatswesen klar gemacht“ werden Sie beim Lesen von Nachrichten nicht mehr von Überlegungen abgelenkt, was diese oder jene Begriffe zu bedeuten haben.</p>
        <p>Sie bilden außerdem faktenbasiert eine eigene, gut begründete Meinung und können politische Diskussionen auf Augenhöhe verfolgen und sogar souverän führen.</p>
        <p>Sie erkennen die Probleme der aktuellen Politik und können somit frühzeitig erkennen was für berufliche wie private Folgen auf Ihr Leben haben könnte.</p>
        <p>Mit Ihrem Wissen können Sie andere Menschen aufklären und für die Zusammenhänge der aktuellen Lage begeistern.</p>
        <div class="blurb-call">
          <span>Worauf warten Sie noch?</span>
          <span>Gestalten Sie jetzt<br>unsere Zukunft mit!</span>
        </div>
      </div>
    </section>

    <section class="spine">
      <div class="spine-title">STAATSWESEN KLAR GEMACHT <small>Das Politik Buch für Einsteiger</small></div>
      <div class="spine-author">Kilian<br>Sturmfeld</div>
    </section>

    <section class="front">
      <div class="publisher">Verlinda</div>
      <h1 class="title">
        <span class="title-line long">Staatswesen</span>
        <span class="title-meta">Ratgeber</span>
        <span class="title-line">Klar</span>
        <span class="title-meta">Kilian Sturmfeld</span>
        <span class="title-line">Gemacht</span>
      </h1>
      <div class="cover-art" role="img" aria-label="Illustration: Person mit großem Stift vor Stimmzettel mit den Feldern NO und YES, YES angekreuzt"></div>
      <div class="tagline">Das Politik Buch<br>für Einsteiger</div>
      <p class="subtitle">Wie Sie endlich mitreden, Ihr Wissen über die deutsche Politik auffrischen und das Land mitgestalten können!</p>
    </section>
  </div>
</body>
</html>
```